Vell Partners Building Business Cards

We need a business card that reflects our business as "Solar Experts" in San Diego. Browse our website www.vellpartners.example our License needs to be displayed as "CSLB# 4718392" our phone number is (619) 555-0147

Save thousands on your electric bills and increase the value of your home while helping to protect the environment. Our solar installation experts will help you design the system that's right for you, using only the highest quality equipment that will look great and give you ideal performance. Our goal is to make you energy independent, and get your electric bill to 0.

Tobias Wrenfield
(619) 555-0147
tobias@vellpartners.example

Target Market(s)

Home owners in san diego looking for solar

Industry/Entity Type

Solar Energy

Contact Information for Business Card

Tobias Wrenfield
(619) 555-0147
tobias@vellpartners.example

Font styles to use
Other font styles liked:
• Use our logo font

Requirements
Must have
• License needs to be displayed as "CSLB# 4718392" our phone number is (619) 555-0147
Nice to have
• Real images of rooftop home solar in san diego
Should not have
• our business address

```html
<!DOCTYPE html>
<html lang="en">
<head>
<meta charset="utf-8">
<title>Vell Partners Building Business Cards</title>
<link rel="stylesheet" href="https://fonts.googleapis.com/css2?family=Open+Sans:wght@400;600;700&display=swap">
<style>
  :root {
    --backdrop: #1c1c1c;
    --card-white: #f3f3f3;
    --card-gold: #f9ad00;
    --navy: #1f3f7f;
    --ink: #1e1e1e;
  }
  * { margin: 0; padding: 0; box-sizing: border-box; }
  html, body {
    width: 1200px;
    height: 900px;
    overflow: hidden;
    background: var(--backdrop);
    font-family: "Open Sans", Arial, sans-serif;
  }
  .canvas {
    position: relative;
    width: 1200px;
    height: 900px;
  }
  .card {
    position: absolute;
    top: 184px;
    height: 490px;
    border-radius: 12px;
    overflow: hidden;
  }
  .card-front {
    left: 299px;
    width: 301px;
    background: var(--card-white);
  }
  .card-back {
    left: 645px;
    width: 305px;
    background: var(--card-gold);
  }
  .brand-mark {
    position: absolute;
    left: 0;
    right: 0;
    top: 92px;
    display: flex;
    flex-direction: column;
    align-items: center;
    gap: 16px;
  }
  .brand-dot {
    width: 84px;
    height: 84px;
    border-radius: 50%;
    background: var(--card-gold);
  }
  .brand-name {
    color: var(--navy);
    font-weight: 700;
    font-size: 20px;
    letter-spacing: 0.2px;
  }
  .contact {
    position: absolute;
    left: 0;
    right: 0;
    top: 300px;
    text-align: center;
    color: var(--ink);
    font-size: 14px;
    line-height: 19px;
  }
  .contact-name {
    color: var(--navy);
    font-weight: 600;
    font-size: 16px;
    text-transform: uppercase;
    margin-bottom: 21px;
  }
  .contact-license { margin-bottom: 10px; }
  .contact-license .label {
    color: var(--navy);
    font-weight: 700;
    font-size: 15px;
  }
  .wordmark {
    position: absolute;
    left: 50%;
    top: 50%;
    transform: translate(-50%, -50%) rotate(-90deg);
    white-space: nowrap;
    text-align: center;
    color: var(--navy);
    font-weight: 700;
    font-size: 46px;
    line-height: 50px;
    letter-spacing: -1px;
  }
</style>
</head>
<body>
<main class="canvas">
  <section class="card card-front">
    <div class="brand-mark">
      <span class="brand-dot"></span>
      <span class="brand-name">Vell Partners Building</span>
    </div>
    <div class="contact">
      <p class="contact-name">Tobias Wrenfield</p>
      <p class="contact-license"><span class="label">License:</span> CSLB# 4718392</p>
      <p class="contact-phone">(619) 555-0147</p>
      <p class="contact-email">tobias@vellpartners.example</p>
    </div>
  </section>
  <section class="card card-back">
    <p class="wordmark">Vell Partners<br>Building</p>
  </section>
</main>
</body>
</html>
```